Business Card Design

Company is a Commercial Building Company specialising in New Construction and existing refurbishments

Industry/Entity Type

Business

Contact Information for Business Card

Dale Mercer
Construction Manager
E Dale@harbridgebuilding.com.au
M 0400 213 947
Mail 27 Tarrant Rise Kellmoor WA 6192

```html
<!DOCTYPE html>
<html lang="en">
<head>
<meta charset="utf-8">
<title>Harbridge Building &amp; Construction – Business Card</title>
<link rel="stylesheet" href="https://fonts.googleapis.com/css2?family=Roboto+Condensed:ital,wght@0,400;0,700;1,400&display=swap">
<style>
  :root {
    --slate: #3d4759;
    --slate-deep: #353e4f;
    --teal: #17a9cb;
    --orange: #ec7a1c;
    --white: #ffffff;
    --paper: #f7f7f6;
    --backdrop: #e7e4df;
  }
  * { margin: 0; padding: 0; box-sizing: border-box; }
  html, body {
    width: 1200px; height: 804px; overflow: hidden;
    background: var(--backdrop);
    font-family: "Roboto Condensed", Arial, sans-serif;
  }
  .stage { position: relative; width: 1200px; height: 804px; }
  .card {
    position: absolute; top: 257px;
    width: 478px; height: 288px; overflow: hidden;
    box-shadow: 0 3px 10px rgba(0,0,0,.22);
  }
  .card--front { left: 108px; background: var(--slate); }
  .card--back { left: 613px; background: var(--paper); }

  .wordmark {
    position: absolute;
    font-weight: 700; line-height: 1.12;
    text-transform: uppercase;
  }
  .card--front .wordmark {
    left: 0; right: 0; top: 178px;
    text-align: center; color: var(--white); font-size: 22px;
  }
  .card--back .wordmark {
    left: 52px; top: 138px;
    color: var(--slate); font-size: 20px;
  }
  .wordmark span { display: block; }

  .band {
    position: absolute; left: 0; right: 0; top: 190px; bottom: 0;
    background: linear-gradient(180deg, var(--slate) 0%, var(--slate-deep) 100%);
  }

  .person { position: absolute; right: 22px; top: 43px; text-align: right; }
  .person__name {
    color: var(--slate); font-weight: 700; font-size: 19px; letter-spacing: 1.5px;
    text-transform: uppercase;
  }
  .person__role { color: var(--orange); font-style: italic; font-size: 13px; margin-top: 1px; }

  .contact {
    position: absolute; right: 20px; top: 200px;
    list-style: none; text-align: right;
    color: var(--white); font-size: 12px; line-height: 18.5px;
  }
  .contact li { display: flex; justify-content: flex-end; align-items: center; gap: 6px; }
  .contact svg { width: 11px; height: 11px; flex: none; }
  .icon-fill { fill: var(--teal); }
  .icon-line { fill: none; stroke: var(--teal); stroke-width: 1.2; }
</style>
</head>
<body>
<main class="stage">
  <section class="card card--front" aria-label="Card front">
    <p class="wordmark"><span>Harbridge Building</span><span>&amp; Construction</span></p>
  </section>

  <section class="card card--back" aria-label="Card back">
    <div class="band" role="img" aria-label="Decorative band in slate with teal and orange accents"></div>

    <p class="wordmark"><span>Harbridge Building</span><span>&amp; Construction</span></p>

    <div class="person">
      <p class="person__name">Dale Mercer</p>
      <p class="person__role">Construction Manager</p>
    </div>

    <ul class="contact">
      <li>0400 213 947
        <svg viewBox="0 0 12 12" aria-hidden="true"><path class="icon-fill" d="M3,0h6a1,1 0 0 1 1,1v10a1,1 0 0 1-1,1H3a1,1 0 0 1-1-1V1a1,1 0 0 1 1-1zM3.5,1.5v8h5v-8z"/></svg></li>
      <li>dale@harbridgebuilding.com.au
        <svg viewBox="0 0 12 12" aria-hidden="true"><path class="icon-fill" d="M0,2h12v8H0zM1,3l5,4 5-4z"/></svg></li>
      <li>www.harbridgebuilding.com.au
        <svg viewBox="0 0 12 12" aria-hidden="true"><g class="icon-line"><circle cx="6" cy="6" r="5.2"/><ellipse cx="6" cy="6" rx="2.2" ry="5.2"/><path d="M0.8,6h10.4"/></g></svg></li>
      <li>27 Tarrant Rise Kellmoor WA 6192
        <svg viewBox="0 0 12 12" aria-hidden="true"><path class="icon-fill" d="M6,0a4.2,4.2 0 0 1 4.2,4.2C10.2,7.4 6,12 6,12S1.8,7.4 1.8,4.2A4.2,4.2 0 0 1 6,0zM6,2.6a1.6,1.6 0 1 0 0,3.2a1.6,1.6 0 1 0 0-3.2z"/></svg></li>
    </ul>
  </section>
</main>
</body>
</html>
```